Powerpoint template for basic scientists studying immunology

We are an QFB-funded consortium of basic science researchers at academic centers in Boston, Philadelphia and Oxford, UK. We study why the immune system fails to get rid of Hepatitis C virus, and whether new antiviral treatments that reduce viral load improve immune function. We are looking for a powerpoint template that we can use as a "brand" for our research consortium. It would feature a logo (file attached) and should represent the fonts/colors contained in the logo. We we would present at meetings and to program officers at the QFB, but, if we ever get around to it, would also be on a website.

The scientific description is as follows:
Hepatitis C virus (HCV) infects 185 million persons worldwide, is the leading indication for liver transplantation and, in the US, has a higher mortaliy rate than HIV. The annual healthcare costs associated with HCV exceed $9 billion, a number expected to increase as the epidemic matures and end stage liver disease peaks over the next decade. By virtue of its remarkable predilection for persistence, HCV is a model chronic viral infection. Mounting evidence supports the idea that HCV, while inducing type I IFN expression, maintains chronicity by virtue of global suppression of host innate and adaptive immunity. The mainstay of treatment for the last two decades, IFN-α-based regimens are ineffective in many patient subgroups and have significant side effects. The recent development of highly effective direct acting antivirals (DAA) against HCV promises to alter the landscape of this devastating infection by offering curative therapy without IFN. However, it remains essential that we understand what type of immunity remains following pharmacological eradication of the virus because: a) many HCV infected subjects remain at risk for re-infection; and b) DAAs are only partially effective in some patient subgroups, particularly those with past treatment with IFN. The imminent availability of IFN-free treatment for HCV offers an unprecedented opportunity to understand broad questions about alterations in immunity in humans with cure of chronic infections. Until now, mechanistic dissection of human immune responses has been challenging due to limited ability to directly perturb the system. The organizing principle of this U19 Program therefore, is to capitalize on the unique opportunity to, for the first time, cure chronic viral infection in humans without immune modulation and interrogate the immunological changes that ensue. Thus, we have formulated the following central hypothesis for this Program: DAA-mediated cure of chronic HCV infection will lead to partial "resetting" of some immune abnormalities, but specific immunological defects will persist in some subjects that prevent development of optimal immunity to HCV. We will test this hypothesis through a set of integrated Projects and Cores.

Target Market(s)

scientists.

Industry/Entity Type

Biotechnology

Font styles to use
Sans Serif

Requirements
Must have
• Very clean, very simple. Mostly whitespace for puting graphs and data on. Colors, fonts should match the logo. Please see ppt example.
Should not have
• too much of the ppt covered with the logo.

```html
<!DOCTYPE html>
<html lang="en">
<head>
<meta charset="utf-8">
<title>Consortium Slide Template</title>
<link href="https://fonts.googleapis.com/css2?family=Arimo:wght@400;700&family=Carlito:wght@400;700&display=swap" rel="stylesheet">
<style>
  :root {
    --stage: #000000;
    --paper: #ffffff;
    --blue: #1b9bd7;
    --green: #74b944;
    --grey: #7b7b7b;
    --ink: #1a1a1a;
    --rule: #555555;
    --row-tint: #dfe2d3;
    --row-line: #c9ceb8;
    --haze: #f1f2f3;
  }
  * { margin: 0; padding: 0; box-sizing: border-box; }
  html, body { width: 924px; height: 1200px; overflow: hidden; background: var(--stage); }
  body { position: relative; font-family: "Arimo", Arial, sans-serif; color: var(--ink); }

  .slide { position: absolute; width: 750px; height: 562px; background: var(--paper); overflow: hidden; }
  .slide--six { left: 97px; top: 26px; }
  .slide--seven { left: 102px; top: 602px; width: 745px; height: 558px; }

  .corner-haze { position: absolute; right: 0; top: 0; width: 230px; height: 200px;
    background: radial-gradient(ellipse at 80% 20%, var(--haze) 0%, rgba(241,242,243,0.6) 50%, rgba(255,255,255,0) 80%); }

  .header-bar { position: absolute; left: 85px; top: 0; width: 4px; height: 64px; background: var(--green); }
  .header-kicker { position: absolute; left: 102px; top: 26px; font-size: 16px; color: var(--green); letter-spacing: 0.1px; }
  .header-date { position: absolute; left: 102px; top: 46px; font-size: 15px; font-weight: 700; }

  .page-badge { position: absolute; left: 692px; top: 19px; width: 48px; height: 46px; }
  .page-badge span { position: absolute; inset: 0; display: flex; align-items: center; justify-content: center;
    color: #fff; font-size: 16px; }

  .slide-title { position: absolute; left: 83px; top: 128px; font-size: 38px; font-weight: 700; color: var(--blue); }

  .cycle { position: absolute; left: 0; top: 0; width: 400px; height: 480px; }
  .cycle text { font-family: "Arimo", Arial, sans-serif; font-size: 16px; text-anchor: middle; }

  .bullets { position: absolute; left: 382px; top: 206px; width: 345px; list-style: none; }
  .bullets li { position: relative; padding-left: 11px; font-size: 13.4px; line-height: 16.3px; margin-bottom: 17px; }
  .bullets li::before { content: ""; position: absolute; left: 0; top: 2px; width: 5px; height: 5px; border-radius: 50%; background: var(--green); }

  .brand-mark { position: absolute; display: flex; flex-direction: column; align-items: center; width: 100px; }
  .brand-mark .dot { width: 26px; height: 26px; border-radius: 50%; background: var(--blue); margin-bottom: 6px; }
  .brand-mark .name { font-size: 14px; color: var(--grey); letter-spacing: 0.3px; }
  .slide--six .brand-mark { left: 615px; top: 482px; }
  .slide--seven .brand-mark { left: 608px; top: 458px; }

  .footer-rule { position: absolute; left: 83px; width: 531px; height: 1px; background: var(--rule); }
  .footer-note { position: absolute; left: 83px; font-size: 10px; color: var(--ink); }
  .slide--six .footer-rule { top: 515px; }
  .slide--six .footer-note { top: 521px; }
  .slide--seven .footer-rule { top: 510px; width: 528px; }
  .slide--seven .footer-note { top: 516px; }

  .data-table { position: absolute; left: 87px; top: 174px; width: 430px; border-collapse: collapse;
    font-family: "Carlito", Calibri, sans-serif; font-size: 13.5px; box-shadow: 1px 1px 2px rgba(0,0,0,0.25); }
  .data-table th { background: var(--blue); color: var(--ink); font-weight: 700; height: 47px;
    border: 2px solid #0d2b45; border-left-color: #0d2b45; }
  .data-table td { text-align: center; border: 2px solid #fff; border-bottom-color: var(--row-line); line-height: 17px; }
  .data-table td:first-child, .data-table th:first-child { width: 107px; }
  .data-table tr.tint td { background: var(--row-tint); }
  .data-table tr.plain td { background: #fff; border-left-color: var(--row-line); border-right-color: var(--row-line); }
  .r1 td { height: 46px; } .r2 td { height: 46px; } .r3 td { height: 45px; }
  .r4 td { height: 29px; } .r5 td { height: 63px; } .r6 td { height: 28px; }

  .side-copy { position: absolute; left: 590px; top: 226px; width: 150px; font-size: 12.2px; line-height: 14.9px; text-align: center; }
</style>
</head>
<body>

<section class="slide slide--six">
  <div class="corner-haze" role="img" aria-label="Faint decorative background tint"></div>
  <div class="header-bar"></div>
  <p class="header-kicker">PPT HEADING GOES HERE</p>
  <p class="header-date">JUNE,2015</p>
  <div class="page-badge">
    <svg width="48" height="46" viewBox="0 0 48 46"><polygon points="12,0 36,0 48,23 36,46 12,46 0,23" fill="#7b7b7b"/></svg>
    <span>06</span>
  </div>
  <h1 class="slide-title">Information Graphics</h1>

  <svg class="cycle" viewBox="0 0 400 480">
    <g fill="#8a8a8a">
      <polygon points="0,-7 10,-7 10,-13 22,0 10,13 10,7 0,7" transform="translate(240,276) rotate(45)"/>
      <polygon points="0,-7 10,-7 10,-13 22,0 10,13 10,7 0,7" transform="translate(260,356) rotate(135)"/>
      <polygon points="0,-7 10,-7 10,-13 22,0 10,13 10,7 0,7" transform="translate(180,374) rotate(225)"/>
      <polygon points="0,-7 10,-7 10,-13 22,0 10,13 10,7 0,7" transform="translate(160,296) rotate(315)"/>
    </g>
    <circle cx="210" cy="245" r="39" fill="#1b9bd7"/>
    <circle cx="130" cy="324" r="39" fill="#74b944"/>
    <circle cx="289" cy="324" r="39" fill="#74b944"/>
    <circle cx="210" cy="405" r="39" fill="#1b9bd7"/>
    <g fill="#ffffff">
      <text x="210" y="237">TEXT</text><text x="210" y="263">HERE</text>
      <text x="130" y="316">TEXT</text><text x="130" y="343">HERE</text>
      <text x="289" y="316">TEXT</text><text x="289" y="343">HERE</text>
      <text x="210" y="397">TEXT</text><text x="210" y="424">HERE</text>
    </g>
    <g fill="#1a1a1a">
      <text x="210" y="310">YOUR</text><text x="210" y="333">TEXT</text><text x="210" y="356">HERE</text>
    </g>
  </svg>

  <ul class="bullets">
    <li>Corporate network So they can quickly Identify and address Suspicious activity On the network That could lead to</li>
    <li>Corporate network So they can quickly Identify and address Suspicious activity On the network That could lead to</li>
    <li>Corporate network So they can quickly Identify and address Suspicious activity On the network That could lead to</li>
    <li>Corporate network So they can quickly Identify and address Suspicious activity On the network That could lead to</li>
  </ul>

  <div class="brand-mark"><span class="dot"></span><span class="name">HVIR LAB</span></div>
  <div class="footer-rule"></div>
  <p class="footer-note">© 2015 HVIR LAB CONSORTIUM</p>
</section>

<section class="slide slide--seven">
  <div class="corner-haze" role="img" aria-label="Faint decorative background tint"></div>
  <div class="header-bar"></div>
  <p class="header-kicker">PPT HEADING GOES HERE</p>
  <p class="header-date">JUNE,2015</p>
  <div class="page-badge" style="left:688px">
    <svg width="48" height="46" viewBox="0 0 48 46"><polygon points="12,0 36,0 48,23 36,46 12,46 0,23" fill="#7b7b7b"/></svg>
    <span>07</span>
  </div>
  <h1 class="slide-title" style="top:120px">Your graph here</h1>

  <table class="data-table">
    <thead>
      <tr><th></th><th>2011-2012</th><th>2012-2013</th><th>2013-2018E</th></tr>
    </thead>
    <tbody>
      <tr class="tint r1"><td>North America</td><td>8.9</td><td>15.6</td><td>3.3</td></tr>
      <tr class="plain r2"><td>Latin America</td><td>11.4</td><td>11.1</td><td>8.8</td></tr>
      <tr class="tint r3"><td>Western<br>Europe</td><td>5.0</td><td>5.2</td><td>3.3</td></tr>
      <tr class="plain r4"><td>Japan</td><td>2.8</td><td>4.8</td><td>1.2</td></tr>
      <tr class="tint r5"><td>Asia-Pacific<br>(ex-Japan)</td><td>16.2</td><td>30.5</td><td>10.5</td></tr>
      <tr class="plain r6"><td>Global</td><td>8.7</td><td>14.6</td><td>5.4</td></tr>
    </tbody>
  </table>

  <p class="side-copy">Corporate network So they can quickly Identify and address Suspicious activity On the network That could lead to Corporate network So they can quickly Identify and address Suspicious activity On the network That could lead to Corporate network So they can quickly Identify and address Suspicious activity On the network That could lead to</p>

  <div class="brand-mark"><span class="dot"></span><span class="name">HVIR LAB</span></div>
  <div class="footer-rule"></div>
  <p class="footer-note">© 2015 HVIR LAB CONSORTIUM</p>
</section>

</body>
</html>
```